Venture Capital Firm Needs Website Redesign

We need a bold revamp of our website (https://halvenmoor.vc/)
which at the moment looks washed out. We want a crisp, fresh and unique look. Feel free to keep as much or as little content in the site. The only thing we need to keep is a team section. The site should convey a clear distinction between our 3 product lines: Venture Capital, Private Credit, and Crypto. Two versions of our logo are attached and they should not change. For design inspirations, we like http://www.plumridgecap.com/ for a more simple site and for a more built out site we like http://tallowgate.com/

Updates
Industry/Entity Type
Investment
Coding
Coded - Design and coding required
Number of Pages Required
1 page
Font styles to use
Colors
Designer to choose colors to be used in the design.
Requirements
Must have
- - Clear distinction between our 3 product lines: Venture Capital, Private Credit
- - Team section

Nice to have
- Some really creative aspect like http://www.plumridgecap.com/ has with the distinction between first, second, and third kind

```html
<!DOCTYPE html>
<html lang="en">
<head>
<meta charset="utf-8">
<title>Halvenmoor — One Page Site</title>
<link rel="stylesheet" href="https://fonts.googleapis.com/css2?family=Open+Sans:wght@300;400;600&display=swap">
<style>
:root{
  --olive:#6b7a2a;
  --olive-light:#8d9c3c;
  --bg-top:#5f7228;
  --bg-bottom:#2a3300;
  --dark:#1f1f1f;
  --panel-grey:#e2e2e2;
  --text-dark:#2c2c2c;
  --text-body:#555;
  --white:#fff;
}
*{margin:0;padding:0;box-sizing:border-box}
html,body{width:1200px;height:1200px;overflow:hidden}
body{
  font-family:"Open Sans",sans-serif;
  background:linear-gradient(170deg,var(--bg-top),var(--bg-bottom));
  position:relative;
}
.page{position:absolute;left:433px;top:0;width:334px;height:1196px;background:var(--white);overflow:hidden}
.section{position:absolute;left:0;width:334px}
.btn{position:absolute;background:var(--olive);color:var(--white);font-size:5.5px;letter-spacing:.3px;padding:3px 6px;text-transform:uppercase;white-space:nowrap}
.body-copy{position:absolute;font-size:5.6px;line-height:9.4px;color:var(--text-body)}
.heading{position:absolute;font-weight:300;font-size:11px;letter-spacing:.4px;color:var(--text-dark);text-transform:uppercase}

/* nav */
.nav{top:0;height:14px;background:#151515}
.brand{position:absolute;left:14px;top:0;font-size:12px;line-height:14px;font-weight:300;color:var(--white);letter-spacing:.5px}
.nav-links{position:absolute;right:10px;top:4px;display:flex;gap:7px;font-size:4.8px;color:#ccc;letter-spacing:.4px}
.nav-links .active{border:.5px solid #aaa;padding:0 2px}

/* hero */
.hero{top:14px;height:168px;background:linear-gradient(100deg,#2b1a12 0%,#4a2c1e 45%,#6b4a3a 75%,#3a3530 100%)}
.hero-title{position:absolute;top:45px;width:100%;text-align:center;color:var(--white);font-weight:300;font-size:15px;letter-spacing:2.5px}
.hero-text{position:absolute;top:69px;width:100%;text-align:center;color:#ddd;font-size:5.6px;line-height:9.5px}
.dots{position:absolute;top:156px;left:160px;display:flex;gap:3px}
.dots span{width:3px;height:3px;border-radius:50%;background:#888}
.dots span:first-child{background:var(--olive-light)}

/* about */
.about{top:182px;height:154px;background:var(--panel-grey)}
.about-visual{position:absolute;left:142px;top:20px;width:175px;height:108px}
.about-visual .photo{position:absolute;left:6px;top:6px;width:163px;height:96px;background:linear-gradient(120deg,#5b7790,#9aa6ad 55%,#6c7780)}
.overlay-title{position:absolute;left:6px;top:36px;width:163px;text-align:center;color:var(--white);font-size:10px;font-weight:300;letter-spacing:.8px}
.overlay-text{position:absolute;left:20px;top:52px;width:135px;text-align:center;color:#eee;font-size:4.6px;line-height:7.5px}

/* venture capital */
.vc{top:336px;height:102px;background:var(--dark)}
.vc-title{position:absolute;top:12px;width:100%;text-align:center;color:var(--olive-light);font-size:10.5px;font-weight:300;letter-spacing:.6px}
.vc-text{position:absolute;top:27px;width:100%;text-align:center;color:#ccc;font-size:5.6px;line-height:9.5px}
.partners{position:absolute;top:66px;left:0;width:100%;display:flex;justify-content:space-around;align-items:center;padding:0 30px}
.partner{font-size:9px;font-weight:400;color:#4aa8d8}
.partner-mark{width:12px;height:12px;border-radius:50%;background:#6b8f2a}

/* private credit */
.credit{top:438px;height:154px;background:var(--panel-grey)}
.credit-visual{position:absolute;left:142px;top:16px;width:177px;height:110px}
.credit-card{position:absolute;left:6px;top:6px;width:162px;height:96px;background:#d9d9d9;border:1px solid #888}
.credit-logos{position:absolute;top:44px;left:0;width:100%;display:flex;justify-content:space-around;align-items:center;font-size:7px;color:#444;white-space:nowrap}

/* crypto */
.crypto{top:592px;height:154px;background:var(--white)}

/* team */
.team{top:746px;height:352px;background:var(--dark)}
.team-title{position:absolute;top:15px;width:100%;text-align:center;color:var(--olive-light);font-size:11px;font-weight:300;letter-spacing:.6px}
.team-sub{position:absolute;top:29px;width:100%;text-align:center;color:#ccc;font-size:4.8px}
.member{position:absolute;width:93px;height:74px;border:1px solid var(--olive-light);background:radial-gradient(circle at 50% 45%,#9a9a9a,#d8d8d8 70%)}

/* contact */
.contact{top:1098px;height:98px;background:var(--panel-grey)}
.contact-title{position:absolute;left:17px;top:10px;font-size:11px;font-weight:300;color:var(--olive);letter-spacing:.4px}
.contact-lines{position:absolute;left:17px;top:25px;font-size:5.3px;line-height:10px;color:var(--text-body)}
.contact-lines .muted{color:#a9a9a9}
.col-head{position:absolute;font-size:5.5px;color:var(--text-dark)}
.col-small{position:absolute;font-size:4.3px;line-height:6.5px;color:var(--text-body)}
.input{position:absolute;left:113px;top:54px;width:100px;height:10px;background:var(--white);border:.5px solid #ccc;font-size:4.2px;color:#aaa;padding:2px 3px}
.social{position:absolute;left:223px;top:70px;display:flex;gap:8px}
.social span{width:10px;height:10px;border-radius:50%;background:var(--olive)}
</style>
</head>
<body>
<main class="page">

  <header class="section nav">
    <div class="brand">HALVENMOOR</div>
    <nav class="nav-links">
      <span>VENTURE</span><span>PRIVATE CREDIT</span><span class="active">ABOUT US</span><span>TEAM</span><span>BLOG</span>
    </nav>
  </header>

  <section class="section hero" role="img" aria-label="Photo of hands typing on a laptop at a wooden desk, darkened">
    <h1 class="hero-title">LOREM IPSUM</h1>
    <p class="hero-text">dolor sit amet, consectetur adipiscing elit. Integer nec odio. Praesent libero.<br>Sed cursus ante dapibus diam. Sed nisi. Nulla quis sem</p>
    <span class="btn" style="left:143px;top:129px">Learn more</span>
    <div class="dots"><span></span><span></span><span></span></div>
  </section>

  <section class="section about">
    <h2 class="heading" style="left:19px;top:22px">About us</h2>
    <p class="body-copy" style="left:19px;top:36px;width:112px">dolor sit amet, consectetur adipiscing elit. Integer nec odio. Praesent libero. Sed cursus ante dapibus diam. Sed nisi. Nulla quis sem at nibh elementum imperdiet. Duis sagittis ipsum. Praesent mauris. Fusce nec tellus sed augue semper porta. Mauris massa. Vestibulum lacinia arcu eget nulla. Class aptent ...</p>
    <span class="btn" style="left:19px;top:120px">Learn more about us</span>
    <div class="about-visual">
      <svg width="175" height="108" style="position:absolute;left:0;top:0">
        <polygon points="2,4 172,0 175,104 4,108" fill="#3a3a3a" stroke="#6b7a2a" stroke-width="1"/>
      </svg>
      <div class="photo" role="img" aria-label="Desk photo with tablet, notebook and stethoscope, blue-grey toned"></div>
      <div class="overlay-title">LOREM IPSUM</div>
      <div class="overlay-text">dolor sit amet, consectetur adipiscing elit. Integer nec odio. Praesent libero.</div>
    </div>
  </section>

  <section class="section vc">
    <svg width="334" height="102" style="position:absolute;left:0;top:0">
      <defs>
        <linearGradient id="swoosh" x1="0" x2="1"><stop offset="0" stop-color="#6b7a2a"/><stop offset="1" stop-color="#6b7a2a" stop-opacity="0"/></linearGradient>
        <linearGradient id="swoosh2" x1="1" x2="0"><stop offset="0" stop-color="#8d9c3c"/><stop offset="1" stop-color="#8d9c3c" stop-opacity="0"/></linearGradient>
      </defs>
      <path d="M0 0 L0 18 Q100 0 334 2 L334 0 Z" fill="#e2e2e2"/>
      <path d="M0 18 Q100 0 334 2 L334 4 Q110 6 0 24 Z" fill="url(#swoosh)"/>
      <path d="M334 102 L334 80 Q240 98 0 102 Z" fill="#e2e2e2"/>
      <path d="M334 74 Q240 94 0 98 L0 102 Q240 98 334 80 Z" fill="url(#swoosh2)"/>
    </svg>
    <h2 class="vc-title">VENTURE CAPITAL</h2>
    <p class="vc-text">dolor sit amet, consectetur adipiscing elit. Integer nec odio. Praesent libero.<br>Sed cursus ante dapibus diam. Sed nisi. Nulla quis sem at nibh elementum imperdiet.</p>
    <div class="partners">
      <span class="partner">Tinylane</span>
      <span class="partner-mark"></span>
      <span class="partner" style="color:#3fa0a8">Brightfern</span>
      <span class="partner" style="color:#3b6fb0">Norvane</span>
    </div>
  </section>

  <section class="section credit">
    <h2 class="heading" style="left:17px;top:18px">Private credit</h2>
    <p class="body-copy" style="left:17px;top:32px;width:112px">dolor sit amet, consectetur adipiscing elit. Integer nec odio. Praesent libero. Sed cursus ante dapibus diam. Sed nisi. Nulla quis sem at nibh elementum imperdiet. Duis sagittis ipsum. Praesent mauris. Fusce nec tellus sed augue semper porta. Mauris massa. Vestibulum lacinia arcu eget nulla. Class aptent ...</p>
    <span class="btn" style="left:17px;top:121px">Learn more</span>
    <div class="credit-visual">
      <svg width="177" height="110" style="position:absolute;left:0;top:0">
        <polygon points="0,6 174,0 177,106 3,110" fill="#333" stroke="#6b7a2a" stroke-width="1"/>
      </svg>
      <div class="credit-card">
        <div class="credit-logos">
          <span>Quillmere Group</span><span style="color:#8a5aa8">Pixelora</span><span>Stillbank</span>
        </div>
      </div>
    </div>
  </section>

  <section class="section crypto">
    <svg width="180" height="112" style="position:absolute;left:16px;top:22px" role="img" aria-label="Line chart of price rising in steps">
      <rect x="1" y="1" width="150" height="108" fill="#f6f6f6" stroke="#6b7a2a" stroke-width="1.2"/>
      <g stroke="#ddd" stroke-width=".5">
        <line x1="1" y1="20" x2="151" y2="20"/><line x1="1" y1="40" x2="151" y2="40"/><line x1="1" y1="60" x2="151" y2="60"/><line x1="1" y1="80" x2="151" y2="80"/><line x1="1" y1="100" x2="151" y2="100"/>
        <line x1="20" y1="1" x2="20" y2="109"/><line x1="40" y1="1" x2="40" y2="109"/><line x1="60" y1="1" x2="60" y2="109"/><line x1="80" y1="1" x2="80" y2="109"/><line x1="100" y1="1" x2="100" y2="109"/><line x1="120" y1="1" x2="120" y2="109"/><line x1="140" y1="1" x2="140" y2="109"/>
      </g>
      <polyline fill="none" stroke="#5d7a1e" stroke-width="1.2" points="4,100 20,99 30,98 40,96 55,94 60,86 70,85 72,72 82,72 84,58 95,57 97,22 110,20 115,18 125,17 130,16 140,14 143,22 148,12"/>
      <g font-size="4" fill="#777" font-family="Open Sans, sans-serif">
        <text x="154" y="6">80</text><text x="154" y="22">75</text><text x="154" y="42">70</text><text x="154" y="62">65</text><text x="154" y="82">60</text><text x="154" y="102">55</text>
      </g>
    </svg>
    <h2 class="heading" style="left:200px;top:20px">Crypto</h2>
    <p class="body-copy" style="left:200px;top:34px;width:116px">dolor sit amet, consectetur adipiscing elit. Integer nec odio. Praesent libero. Sed cursus ante dapibus diam. Sed nisi. Nulla quis sem at nibh elementum imperdiet. Duis sagittis ipsum. Praesent mauris. Fusce nec tellus sed augue semper porta. Mauris massa. Vestibulum lacinia arcu eget nulla. Class aptent ...</p>
    <span class="btn" style="left:200px;top:124px">Learn more</span>
  </section>

  <section class="section team">
    <svg width="334" height="352" style="position:absolute;left:0;top:0">
      <defs>
        <linearGradient id="teamTop" x1="0" y1="0" x2="0" y2="1"><stop offset="0" stop-color="#4a5620"/><stop offset="1" stop-color="#1f1f1f"/></linearGradient>
      </defs>
      <ellipse cx="167" cy="0" rx="260" ry="48" fill="url(#teamTop)"/>
      <ellipse cx="167" cy="352" rx="260" ry="40" fill="#4a5620" opacity=".5"/>
    </svg>
    <h2 class="team-title">OUR TEAM</h2>
    <p class="team-sub">The very best helping the very best.</p>
    <div class="member" style="left:16px;top:53px" role="img" aria-label="Black and white portrait of team member"></div>
    <div class="member" style="left:120px;top:53px" role="img" aria-label="Black and white portrait of team member"></div>
    <div class="member" style="left:224px;top:53px" role="img" aria-label="Black and white portrait of team member"></div>
    <div class="member" style="left:16px;top:140px" role="img" aria-label="Black and white portrait of team member"></div>
    <div class="member" style="left:120px;top:140px" role="img" aria-label="Black and white portrait of team member"></div>
    <div class="member" style="left:224px;top:140px" role="img" aria-label="Black and white portrait of team member"></div>
    <div class="member" style="left:68px;top:227px" role="img" aria-label="Black and white portrait of team member"></div>
    <div class="member" style="left:173px;top:227px" role="img" aria-label="Black and white portrait of team member"></div>
    <span class="btn" style="left:143px;top:326px">Learn more</span>
  </section>

  <footer class="section contact">
    <h2 class="contact-title">CONTACT US</h2>
    <div class="contact-lines">
      <div class="muted">We would love to hear from you</div>
      <div>info@halvenmoor.vc</div>
      <div>218 Larkspur Ave, Suite 404</div>
      <div>Brookvale, NY</div>
      <div>10417</div>
    </div>
    <div class="col-head" style="left:113px;top:25px">Stay Informed</div>
    <div class="col-small" style="left:113px;top:35px">Subscribe To Our Newsletter</div>
    <div class="input">Enter your Email</div>
    <span class="btn" style="left:113px;top:72px;font-size:4.5px;padding:2px 4px;text-transform:none">Submit</span>
    <div class="col-head" style="left:223px;top:25px">Stay Connected</div>
    <div class="col-small" style="left:223px;top:35px;width:95px">dolor sit amet, consectetur adipiscing elit. Integer nec odio consectetur adipiscing elit. Integer nec odio.</div>
    <div class="social"><span></span><span></span><span></span><span></span></div>
  </footer>

</main>
</body>
</html>
```